Sports League Registration Banner for plimzo

I have a graphic with a basic idea for an ad that I would like to post on plimzo but I need it to be reconfigured to fit their dimensions (1194 by 624, or in that ratio) and to have the text moved and placed in another spot on the ad. I also want the colors to be changed to look like my website (www.tarvoactive.com) but no logo on the ad. This is to promote registration for a sports league.

The idea is basically to get up off the couch and play some sports. The text on the bottom should be moved off to the side and replaced with:

GET FIT HAVE FUN
10 Game Season + Playoffs
1 Game per week
Team Fee $1525
Player Fee $125

Men's Ball Hockey

```html
<!DOCTYPE html>
<html lang="en">
<head>
<meta charset="utf-8">
<title>Men's Ball Hockey – Registration Banner</title>
<link rel="stylesheet" href="https://fonts.googleapis.com/css2?family=Rubik+Dirt&family=Caveat+Brush&family=Anton&display=swap">
<style>
  :root {
    --sky-light: #dfe9ff;
    --sky-mid: #aac3f5;
    --sky-deep: #7f9fe8;
    --card-green: #6e9140;
    --card-edge: #58762f;
    --band-green: #5c7c31;
    --headline-yellow: #f6e47c;
    --detail-white: #f7f7ef;
    --script-green: #1d3410;
    --badge-white: #ffffff;
    --badge-ink: #1a1a1a;
    --photo-warm: #8a5a38;
    --photo-dark: #3a2a20;
    --photo-light: #c89870;
  }
  html, body {
    margin: 0;
    padding: 0;
    width: 1200px;
    height: 627px;
    overflow: hidden;
  }
  .banner {
    position: relative;
    width: 1200px;
    height: 627px;
    overflow: hidden;
    background:
      radial-gradient(ellipse at 50% 55%, var(--sky-light) 0%, var(--sky-mid) 55%, var(--sky-deep) 100%);
  }
  .sky-decoration {
    position: absolute;
    inset: 0;
  }
  .card {
    position: absolute;
    left: 22px;
    top: 30px;
    width: 1156px;
    height: 540px;
    background: var(--card-green);
    border: 2px solid var(--card-edge);
    transform: rotate(-1deg);
    box-shadow: 0 4px 12px rgba(30, 50, 90, 0.35);
  }
  .hero-photo {
    position: absolute;
    left: 24px;
    top: 52px;
    width: 636px;
    height: 460px;
    background:
      radial-gradient(ellipse at 30% 50%, var(--photo-light) 0%, var(--photo-warm) 45%, var(--photo-dark) 100%);
  }
  .headline {
    position: absolute;
    left: 670px;
    top: 8px;
    width: 486px;
    margin: 0;
    text-align: center;
    font-family: "Rubik Dirt", "Anton", sans-serif;
    font-weight: 400;
    font-size: 72px;
    line-height: 78px;
    color: var(--headline-yellow);
    letter-spacing: 1px;
  }
  .details-band {
    position: absolute;
    left: 660px;
    top: 208px;
    width: 496px;
    height: 200px;
    background: var(--band-green);
  }
  .details-list {
    list-style: none;
    margin: 0;
    padding: 18px 0 0;
    text-align: center;
    font-family: "Rubik Dirt", "Anton", sans-serif;
    font-size: 28px;
    line-height: 39px;
    color: var(--detail-white);
    letter-spacing: 0.5px;
  }
  .league-name {
    position: absolute;
    left: 660px;
    top: 420px;
    width: 496px;
    margin: 0;
    text-align: center;
    font-family: "Caveat Brush", cursive;
    font-weight: 400;
    font-size: 48px;
    color: var(--script-green);
  }
  .never-late-badge {
    position: absolute;
    left: 24px;
    top: 352px;
    width: 196px;
    height: 196px;
  }
  .badge-text {
    font-family: "Anton", sans-serif;
    fill: var(--badge-ink);
    text-anchor: middle;
  }
</style>
</head>
<body>
<div class="banner">
  <svg class="sky-decoration" width="1200" height="627" viewBox="0 0 1200 627" aria-hidden="true">
    <g fill="#ffffff" opacity="0.18">
      <polygon points="600,330 0,0 150,0"/>
      <polygon points="600,330 350,0 500,0"/>
      <polygon points="600,330 700,0 850,0"/>
      <polygon points="600,330 1050,0 1200,0"/>
      <polygon points="600,330 1200,250 1200,420"/>
      <polygon points="600,330 900,627 1050,627"/>
      <polygon points="600,330 400,627 250,627"/>
      <polygon points="600,330 0,450 0,300"/>
    </g>
  </svg>

  <section class="card">
    <div class="hero-photo" role="img" aria-label="Photo of a man lounging in an armchair with a burger and a mug of beer beside an old television"></div>

    <h1 class="headline">GET FIT AND<br>HAVE FUN!</h1>

    <div class="details-band">
      <ul class="details-list">
        <li>10 GAME SEASON + PLAYOFFS</li>
        <li>1 GAME PER WEEK</li>
        <li>TEAM FEE $1525</li>
        <li>PLAYER FEE $125</li>
      </ul>
    </div>

    <p class="league-name">Men's Ball Hockey</p>

    <svg class="never-late-badge" viewBox="0 0 200 200" role="img" aria-label="It's never too late">
      <polygon fill="var(--badge-white)" stroke="var(--badge-ink)" stroke-width="2" stroke-dasharray="4 3"
        points="100,4 112,28 134,10 139,37 166,28 162,55 190,55 176,79 198,92 176,107 192,128 166,134 172,161 145,158 142,186 118,174 100,196 82,174 58,186 55,158 28,161 34,134 8,128 24,107 2,92 24,79 10,55 38,55 34,28 61,37 66,10 88,28"/>
      <g transform="rotate(-12 100 100)">
        <text class="badge-text" x="100" y="68" font-size="26">IT'S</text>
        <text class="badge-text" x="100" y="106" font-size="40">NEVER</text>
        <text class="badge-text" x="100" y="128" font-size="20">TOO</text>
        <text class="badge-text" x="100" y="164" font-size="38">LATE</text>
      </g>
    </svg>
  </section>
</div>
</body>
</html>
```